Construction company stationary design

We're wanting to develop a new professional stationary set for a newly establised property related business using our existing logo (attached). Business incorporates renovations, property investment and property development.

Specifically needing letter head, business cards, envelopes, email signature and need to get tshirt and caps embroydered.

Looking for something quite modern but professional using white, black and green.

Investment

```html
<!DOCTYPE html>
<html lang="en">
<head>
<meta charset="utf-8">
<title>Kestrel Constructions – Business Card</title>
<link rel="stylesheet" href="https://fonts.googleapis.com/css2?family=Montserrat:wght@600;700&family=Questrial&display=swap">
<style>
  :root {
    --stage: #2b2b2b;
    --paper: #fbfbf9;
    --brand-green: #78c024;
    --brand-green-dark: #6cb31c;
    --ink: #6b6b6b;
    --ink-strong: #5a5a5a;
    --white: #ffffff;
  }
  * { margin: 0; padding: 0; box-sizing: border-box; }
  html, body { width: 1200px; height: 800px; overflow: hidden; }
  body {
    background: var(--stage);
    font-family: "Questrial", "Century Gothic", sans-serif;
    display: flex;
    flex-direction: column;
    align-items: center;
    justify-content: center;
    gap: 30px;
  }
  .card {
    position: relative;
    width: 630px;
    height: 360px;
    overflow: hidden;
  }

  /* Front */
  .card-front { background: var(--paper); color: var(--ink); }
  .front-wordmark {
    position: absolute;
    left: 70px;
    top: 95px;
    width: 250px;
    text-align: center;
    color: var(--brand-green);
    font-family: "Montserrat", sans-serif;
    font-weight: 700;
    line-height: 1;
  }
  .front-wordmark .name-main { font-size: 50px; letter-spacing: 1px; display: block; }
  .front-wordmark .name-sub { font-size: 17px; letter-spacing: 1.5px; display: block; margin-top: 6px; }
  .front-address {
    position: absolute;
    right: 330px;
    top: 222px;
    text-align: right;
    font-size: 15px;
    line-height: 21px;
  }
  .front-divider {
    position: absolute;
    left: 330px;
    top: 218px;
    width: 1px;
    height: 46px;
    background: #9a9a9a;
  }
  .contact {
    position: absolute;
    left: 372px;
    top: 48px;
    font-size: 14px;
  }
  .contact-name {
    color: var(--brand-green);
    font-family: "Montserrat", sans-serif;
    font-weight: 700;
    font-size: 17px;
    letter-spacing: 0.5px;
  }
  .contact-title { margin-top: 8px; font-size: 14px; }
  .contact-list { margin-top: 26px; display: grid; grid-template-columns: auto auto; column-gap: 5px; row-gap: 2px; }
  .contact-list dt {
    text-align: right;
    font-family: "Montserrat", sans-serif;
    font-weight: 600;
    color: var(--ink-strong);
  }
  .contact-list .gap { margin-top: 18px; }
  .front-rule {
    position: absolute;
    left: 380px;
    right: 0;
    bottom: 24px;
    height: 3px;
    background: var(--brand-green);
  }
  .front-band {
    position: absolute;
    left: 392px;
    right: 0;
    bottom: 0;
    height: 24px;
    background: var(--brand-green);
  }

  /* Back */
  .card-back { background: var(--brand-green); color: var(--white); }
  .back-wordmark {
    position: absolute;
    right: 60px;
    top: 110px;
    text-align: center;
    font-family: "Montserrat", sans-serif;
    font-weight: 700;
    line-height: 1;
  }
  .back-wordmark .name-main { font-size: 54px; letter-spacing: 1px; display: block; }
  .back-wordmark .name-sub { font-size: 18px; letter-spacing: 1.5px; display: block; margin-top: 6px; }
  .back-web {
    position: absolute;
    right: 70px;
    bottom: 70px;
    font-size: 20px;
    letter-spacing: 0.5px;
  }
  .back-web strong { font-family: "Montserrat", sans-serif; font-weight: 700; }
</style>
</head>
<body>
  <section class="card card-front" aria-label="Business card front">
    <div class="front-wordmark">
      <span class="name-main">KESTREL</span>
      <span class="name-sub">CONSTRUCTIONS</span>
    </div>
    <address class="front-address" style="font-style:normal">
      418 Larkspur Ct. Suite 210<br>
      Maple Ridge, CO 80000
    </address>
    <div class="front-divider"></div>
    <div class="contact">
      <div class="contact-name">JORDAN ELLERY</div>
      <div class="contact-title">Chief Manager</div>
      <dl class="contact-list">
        <dt>Phone:</dt><dd>(555) 013-4820</dd>
        <dt>Fax:</dt><dd>(555) 013-4820</dd>
        <dt class="gap">Email:</dt><dd class="gap">info@kestrelbuild.com</dd>
        <dt>Web:</dt><dd>www.kestrelbuild.com</dd>
      </dl>
    </div>
    <div class="front-rule"></div>
    <div class="front-band"></div>
  </section>

  <section class="card card-back" aria-label="Business card back">
    <div class="back-wordmark">
      <span class="name-main">KESTREL</span>
      <span class="name-sub">CONSTRUCTIONS</span>
    </div>
    <div class="back-web">www.<strong>kestrelbuild</strong>.com</div>
  </section>
</body>
</html>
```